Non-governmental organisation branding design

We are looking to get the branding for our new NGO:

Kestrel Harbour Centre

Our tag-line is: Accord through listening

We are a peace brokering organisation that conducts research and offers peace brokering services relating to conflicts around the world.

The branding needs to be simple, to the point and serious.

Other comparable organisations are:

https://www.vantrellhub.org/

http://tlx.fi/

https://www.oravelle.org/

Any questions, please get in touch.

Logo Text

Kestrel Harbour Centre

Number of Pages Required

1 page

```html
<!DOCTYPE html>
<html lang="en">
<head>
<meta charset="UTF-8">
<title>Kestrel Harbour Centre – Business Card</title>
<link href="https://fonts.googleapis.com/css2?family=Questrial&display=swap" rel="stylesheet">
<style>
  :root {
    --backdrop: #34454d;
    --brand-red: #d41f20;
    --card-white: #ffffff;
    --ink: #333333;
    --on-red: #ffffff;
  }
  * { margin: 0; padding: 0; box-sizing: border-box; }
  html, body {
    width: 1200px;
    height: 900px;
    overflow: hidden;
    background: var(--backdrop);
    font-family: "Questrial", sans-serif;
  }
  .canvas {
    position: relative;
    width: 1200px;
    height: 900px;
  }
  .business-card {
    position: absolute;
    left: 100px;
    top: 165px;
    width: 1000px;
    height: 570px;
    display: flex;
    background: var(--card-white);
    box-shadow: 0 18px 40px rgba(0, 0, 0, 0.35);
  }
  .brand-panel {
    width: 440px;
    height: 100%;
    background: var(--brand-red);
    color: var(--on-red);
    display: flex;
    flex-direction: column;
    align-items: center;
    justify-content: center;
    text-align: center;
    padding-bottom: 20px;
  }
  .brand-name {
    font-size: 34px;
    font-weight: 400;
    letter-spacing: 0.5px;
    line-height: 1.1;
    white-space: nowrap;
  }
  .brand-tagline {
    margin-top: 14px;
    font-size: 17px;
    letter-spacing: 4px;
    white-space: nowrap;
  }
  .contact-panel {
    flex: 1;
    padding: 110px 0 0 30px;
  }
  .contact-list { list-style: none; }
  .contact-item {
    display: flex;
    align-items: center;
    margin-bottom: 34px;
    color: var(--ink);
    font-size: 17px;
    letter-spacing: 0.3px;
    line-height: 1.15;
  }
  .contact-icon {
    width: 36px;
    height: 36px;
    flex: none;
    margin-right: 20px;
  }
</style>
</head>
<body>
<div class="canvas">
  <div class="business-card">
    <div class="brand-panel">
      <div class="brand-name">Kestrel Harbour Centre</div>
      <div class="brand-tagline">Accord through listening</div>
    </div>
    <div class="contact-panel">
      <ul class="contact-list">
        <li class="contact-item">
          <svg class="contact-icon" viewBox="0 0 36 36" aria-hidden="true">
            <circle cx="18" cy="18" r="17" fill="var(--brand-red)"/>
            <path d="M18 8a7 7 0 0 0-7 7c0 5 7 12 7 12s7-7 7-12a7 7 0 0 0-7-7z" fill="#fff"/>
            <circle cx="18" cy="15" r="2.8" fill="var(--brand-red)"/>
          </svg>
          <span>Address line 1<br>address line 2</span>
        </li>
        <li class="contact-item">
          <svg class="contact-icon" viewBox="0 0 36 36" aria-hidden="true">
            <circle cx="18" cy="18" r="17" fill="var(--brand-red)"/>
            <path d="M11 10c1.5-1.5 3-1.5 4 0l2 3c.6 1 .3 2-.6 2.7l-1.2 1c1 2.5 2.8 4.3 5.2 5.3l1-1.2c.7-.9 1.7-1.2 2.7-.6l3 2c1.5 1 1.5 2.5 0 4-2 2-5 2.3-9-.5-3.5-2.5-6-5.5-7.5-8.5-1.5-3-1.2-5.5.4-7.2z" fill="#fff"/>
          </svg>
          <span>+65 XXXX XXXX</span>
        </li>
        <li class="contact-item">
          <svg class="contact-icon" viewBox="0 0 36 36" aria-hidden="true">
            <circle cx="18" cy="18" r="17" fill="var(--brand-red)"/>
            <g fill="none" stroke="#fff" stroke-width="1.8">
              <circle cx="18" cy="18" r="10"/>
              <ellipse cx="18" cy="18" rx="4.5" ry="10"/>
              <line x1="8" y1="18" x2="28" y2="18"/>
              <path d="M10 12.5h16M10 23.5h16"/>
            </g>
          </svg>
          <span>www.kestrelharbourcentre.com</span>
        </li>
      </ul>
    </div>
  </div>
</div>
</body>
</html>
```